I need a wine label for a new winery called "Chateau Verelline".
I am looking for an old french style label with a sketched image of a vineyard with the goat with the missing horn somewhat discreetly in the image. Also I want the label to read in much smaller print "Quiet Brook Vineyards". Perhaps in a courtyard the goat with the missing horn is kneeling beside an old wine press. Please see images for examples. P.S. "Verelline" is the goat that fed baby Zeus in mythology. He broke off her horn and it became the horn of pleanty (cornucopia).

Industry/Entity Type

Vineyard

Font styles to use
Script

Requirements
Must have
• sketched image on an off white/white/yellow label
Nice to have
• Nice to have the vineyard with the goat missing a horn kneeling by the old wine press

```html
<!DOCTYPE html>
<html lang="en">
<head>
<meta charset="utf-8">
<title>Chateau Verelline — Cabernet Sauvignon Label</title>
<link href="https://fonts.googleapis.com/css2?family=Pinyon+Script&family=Cormorant+Garamond:ital,wght@0,500;0,600;0,700;1,500&family=Libre+Baskerville&display=swap" rel="stylesheet">
<style>
  :root {
    --page: #fcfaee;
    --label-light: #f1eee0;
    --label-mid: #e6e3d4;
    --label-shade: #cfd0c8;
    --ink: #141414;
    --ink-soft: #2b2b2b;
    --wine-red: #a3262b;
    --sketch-light: #c9c9c2;
    --sketch-dark: #3a3f45;
  }
  html, body {
    margin: 0;
    padding: 0;
    width: 1200px;
    height: 2171px;
    overflow: hidden;
    background: var(--page);
  }
  .canvas {
    position: relative;
    width: 1200px;
    height: 2171px;
  }
  .wine-label {
    position: absolute;
    left: 180px;
    top: 448px;
    width: 840px;
    height: 1276px;
    background: linear-gradient(90deg, var(--label-light) 0%, var(--label-mid) 55%, var(--label-shade) 100%);
    color: var(--ink);
    text-align: center;
  }
  .wine-label > * {
    position: absolute;
    left: 0;
    right: 0;
    margin: 0;
  }
  .estate-name {
    top: 190px;
    font-family: "Pinyon Script", cursive;
    font-weight: 400;
    font-size: 150px;
    line-height: 1;
  }
  .estate-type {
    top: 340px;
    font-family: "Cormorant Garamond", serif;
    font-weight: 600;
    font-size: 52px;
    letter-spacing: 7px;
    line-height: 1;
  }
  .vineyard-sketch {
    left: 250px;
    right: auto;
    top: 480px;
    width: 440px;
    height: 360px;
    background: radial-gradient(ellipse at 45% 45%, var(--sketch-light) 0%, #8f9397 45%, var(--sketch-dark) 100%);
    opacity: 0.85;
  }
  .established {
    left: 556px;
    right: auto;
    top: 808px;
    font-family: "Cormorant Garamond", serif;
    font-style: italic;
    font-weight: 500;
    font-size: 28px;
    color: var(--ink-soft);
    line-height: 1;
  }
  .varietal {
    top: 948px;
    font-family: "Libre Baskerville", serif;
    font-size: 38px;
    color: var(--wine-red);
    line-height: 1;
  }
  .producer {
    top: 1064px;
    font-family: "Cormorant Garamond", serif;
    font-weight: 600;
    font-size: 58px;
    letter-spacing: 2px;
    line-height: 1;
  }
  .producer-sub {
    top: 1124px;
    font-family: "Cormorant Garamond", serif;
    font-weight: 600;
    font-size: 21px;
    letter-spacing: 9px;
    line-height: 1;
  }
  .region {
    top: 1182px;
    font-family: "Cormorant Garamond", serif;
    font-style: italic;
    font-weight: 600;
    font-size: 24px;
    letter-spacing: 5px;
    color: var(--ink-soft);
    line-height: 1;
  }
</style>
</head>
<body>
  <main class="canvas">
    <section class="wine-label">
      <h1 class="estate-name">Verelline</h1>
      <p class="estate-type">CHATEAU</p>
      <div class="vineyard-sketch" role="img" aria-label="Engraved sketch of a vineyard courtyard with a one-horned goat kneeling beside an old wine press"></div>
      <p class="established">est. 2016</p>
      <p class="varietal">CABERNET SAUVIGNON</p>
      <p class="producer">QUIET BROOK</p>
      <p class="producer-sub">VINEYARDS</p>
      <p class="region">GOLDEN MILE</p>
    </section>
  </main>
</body>
</html>
```